Larkmoor Health- Core Values Graphic for Visual Appeal

I would like a poster that could take these written core values from our organization and create a graphic that we could use for our staff and employees. I would also like to incorporate our branding into this project. Thank you!

Target Market(s)

To helps patients and employees understand the core values of our organization

Industry/Entity Type

Healthcare

Requirements
Must have
• Match our branding
Nice to have
• Please use your creativity!
Should not have
• Overly complex/ busy

```html
<!DOCTYPE html>
<html lang="en">
<head>
<meta charset="utf-8">
<title>Larkmoor Health – Core Values</title>
<link rel="stylesheet" href="https://fonts.googleapis.com/css2?family=Montserrat:wght@800&family=Fredoka:wght@600&family=Roboto:wght@400;700&display=swap">
<style>
  :root {
    --ink: #111111;
    --grey: #9a9a9a;
    --brand-blue: #29a8e0;
    --brand-dark: #444444;
    --family: #e6317a;
    --excellence: #9cc96b;
    --integrity: #1f5fa8;
    --service: #9b1f7e;
    --footer: #000000;
    --white: #ffffff;
  }
  * { margin: 0; padding: 0; box-sizing: border-box; }
  html, body { width: 1200px; height: 848px; overflow: hidden; background: var(--white); }
  .poster { position: relative; width: 1200px; height: 848px; font-family: "Roboto", sans-serif; color: var(--ink); }

  .brand { position: absolute; left: 58px; top: 92px; display: flex; align-items: center; gap: 8px; }
  .brand-dot { width: 16px; height: 16px; border-radius: 50%; background: var(--brand-blue); }
  .brand-name { font-family: "Roboto", sans-serif; font-weight: 700; font-size: 20px; color: var(--brand-dark); line-height: 1.1; width: 100px; }

  .title { position: absolute; left: 234px; top: 42px; font-family: "Montserrat", sans-serif; font-weight: 800; font-size: 66px; line-height: 74px; letter-spacing: 0; }

  .intro { position: absolute; left: 553px; top: 42px; width: 620px; font-size: 23px; line-height: 28.4px; color: var(--grey); white-space: nowrap; }
  .intro strong { font-weight: 700; }

  .values-art { position: absolute; left: 0; top: 200px; width: 1200px; height: 260px; }
  .value-heading { font-family: "Fredoka", sans-serif; font-weight: 600; font-size: 38px; letter-spacing: 3px; }

  .columns { position: absolute; left: 0; top: 472px; width: 1200px; }
  .value-text { position: absolute; top: 0; width: 250px; font-size: 14.6px; line-height: 19.9px; letter-spacing: 0.3px; white-space: nowrap; }
  .value-text p + p { margin-top: 19.9px; }
  .value-text b { font-weight: 700; }
  .family-text { left: 53px; } .family-text b { color: var(--family); }
  .excellence-text { left: 350px; } .excellence-text b { color: var(--excellence); }
  .integrity-text { left: 648px; } .integrity-text b { color: var(--integrity); }
  .service-text { left: 946px; } .service-text b { color: var(--service); }

  .footer { position: absolute; left: 0; top: 802px; width: 1200px; height: 46px; background: var(--footer); color: var(--white); display: flex; justify-content: space-between; align-items: center; padding: 0 42px; font-weight: 700; font-size: 12.8px; letter-spacing: 1.2px; }
</style>
</head>
<body>
<div class="poster">
  <div class="brand">
    <span class="brand-dot"></span>
    <span class="brand-name">Larkmoor Health</span>
  </div>

  <h1 class="title">CORE<br>VALUES</h1>

  <p class="intro">These core values are the spirit of who we are as a<br>healthcare team. They guide our actions, unite us in<br>purpose, and ensure that we provide world-class care<br>while <strong>fostering a positive and supportive atmosphere</strong><br>within our team.</p>

  <svg class="values-art" viewBox="0 200 1200 260" xmlns="http://www.w3.org/2000/svg">
    <defs>
      <linearGradient id="g-family" x1="0" x2="1"><stop offset="0" stop-color="#f9c089"/><stop offset="1" stop-color="#ef7c80"/></linearGradient>
      <linearGradient id="g-excellence" x1="0" x2="1"><stop offset="0" stop-color="#e6c83a"/><stop offset="1" stop-color="#a6cb6c"/></linearGradient>
      <linearGradient id="g-integrity" x1="0" x2="1"><stop offset="0" stop-color="#82cdeb"/><stop offset="1" stop-color="#3a84c6"/></linearGradient>
      <linearGradient id="g-service" x1="0" x2="1"><stop offset="0" stop-color="#e3404a"/><stop offset="1" stop-color="#a02778"/></linearGradient>
      <linearGradient id="g-link1" x1="0" x2="1"><stop offset="0" stop-color="#f0848a"/><stop offset="1" stop-color="#e6397c"/></linearGradient>
      <linearGradient id="g-link2" x1="0" x2="1"><stop offset="0" stop-color="#b5cf65"/><stop offset="1" stop-color="#9ecb70"/></linearGradient>
      <linearGradient id="g-link3" x1="0" x2="1"><stop offset="0" stop-color="#3b90d2"/><stop offset="1" stop-color="#2361ac"/></linearGradient>
      <path id="arc-family" d="M 58 296 A 115 115 0 0 1 248 296"/>
      <path id="arc-excellence" d="M 362 300 A 220 220 0 0 1 652 304"/>
      <path id="arc-integrity" d="M 662 300 A 165 165 0 0 1 898 306"/>
      <path id="arc-service" d="M 955 295 A 118 118 0 0 1 1150 297"/>
    </defs>

    <g class="connectors">
      <path fill="url(#g-link1)" d="M153 284 Q302 334 452 284 L452 424 Q302 374 153 424 Z"/>
      <path fill="url(#g-link2)" d="M452 284 Q600 334 748 284 L748 424 Q600 374 452 424 Z"/>
      <path fill="url(#g-link3)" d="M748 284 Q898 334 1047 284 L1047 424 Q898 374 748 424 Z"/>
    </g>

    <g class="rings" fill="#ffffff">
      <circle cx="153" cy="354" r="100"/><circle cx="452" cy="354" r="100"/>
      <circle cx="748" cy="354" r="100"/><circle cx="1047" cy="354" r="100"/>
    </g>

    <circle cx="153" cy="354" r="92" fill="url(#g-family)" role="img" aria-label="Family icon: parents holding a child's hands"/>
    <circle cx="452" cy="354" r="92" fill="url(#g-excellence)" role="img" aria-label="Excellence icon: open hands holding a heart"/>
    <circle cx="748" cy="354" r="92" fill="url(#g-integrity)" role="img" aria-label="Integrity icon: handshake"/>
    <circle cx="1047" cy="354" r="92" fill="url(#g-service)" role="img" aria-label="Service icon: hand supporting a person"/>

    <text class="value-heading" fill="var(--family)"><textPath href="#arc-family" startOffset="50%" text-anchor="middle">FAMILY</textPath></text>
    <text class="value-heading" fill="var(--excellence)"><textPath href="#arc-excellence" startOffset="50%" text-anchor="middle">EXCELLENCE</textPath></text>
    <text class="value-heading" fill="var(--integrity)"><textPath href="#arc-integrity" startOffset="50%" text-anchor="middle">INTEGRITY</textPath></text>
    <text class="value-heading" fill="var(--service)"><textPath href="#arc-service" startOffset="50%" text-anchor="middle">SERVICE</textPath></text>
  </svg>

  <div class="columns">
    <div class="value-text family-text">
      <p>At the heart of our mission is<br>the commitment to provide<br>high-quality, affordable healthca-<br>re in a comforting and uplifting<br><b>family-oriented</b> environment.<br>Just as our community is our<br>extended family, every patient is<br>a cherished member of our<br>healthcare family.</p>
      <p>We treat each individual with the<br>same <b>care</b>, <b>compassion</b>, and<br><b>respect</b> we would offer to our<br>own loved ones.</p>
    </div>
    <div class="value-text excellence-text">
      <p>In line with our goal, we aspire<br>not only to alleviate pain but also<br>to inspire patients to become<br>active participants in their<br>well-being. We believe in<br>empowering our patients through<br><b>education and compassion</b>.</p>
      <p>Our pursuit of excellence is<br>unwavering, driven by our<br>dedication to continuously<br>improve our services at every<br>level, ensuring that our communi-<br>ty receives nothing less than<br><b>exceptional care</b>.</p>
    </div>
    <div class="value-text integrity-text">
      <p>In our healthcare team, Integrity'<br>is non-negotiable. Our purpose<br>is deeply rooted in <b>ethics</b>, integri-<br>ty, and professional standards.<br>We operate with the utmost<br>integrity in every aspect of our<br>work, adhering to the highest<br>ethical principles.</p>
      <p>We understand that <b>trust</b> is the<br>foundation of healthcare, and we<br>are committed to maintaining the<br>trust our community places in us.</p>
    </div>
    <div class="value-text service-text">
      <p>Our vision is grounded in the<br>belief that every person<br>possesses the <b>innate potential</b><br>for true health. We aim to facili-<br>tate the body's <b>natural healing</b><br>response by providing the<br>highest level of service.</p>
      <p>Our hope for each patient<br>extends beyond healing; we<br>aspire to help you fulfill your<br>life's mission and purpose<br>abundantly, <b>supporting you</b><br>in your journey to well-being.</p>
    </div>
  </div>

  <footer class="footer">
    <span>CHIROPRACTIC | MEDICAL | PHYSICAL | THERAPY</span>
    <span>WWW.LARKMOORHEALTH.COM</span>
  </footer>
</div>
</body>
</html>
```